Bookcover: Lessons From the Silent Orchard

I am publishing a super-low-cost innovation book for €4,99 on Bravolo Self Release to help everyone become a great innovator: young ambitious people without college education nor a big budget. Do you want to help me?

Brief:
Design a book cover 1600 x 2560 pixels for BSR.
Main title: Lessons From the Silent Orchard
Sub title: mindset - insights - skills & tools
Author: Maarten de Klerk
Design: captive, and appealing to everyone
Target Group: young ambitious people without college education

For bravolo please format the height/width ratio of 1.6:1

```html
<!DOCTYPE html>
<html lang="en">
<head>
<meta charset="utf-8">
<title>Lessons From the Silent Orchard — Book Cover</title>
<link rel="stylesheet" href="https://fonts.googleapis.com/css2?family=Bebas+Neue&family=Outfit:wght@400;500;600;700&display=swap">
<style>
  :root {
    --page-bg: #ffffff;
    --cover-bg: #f4f4f4;
    --ink-dark: #1f2a3a;
    --ink-text: #2c2c2c;
    --accent-blue: #0a6cf0;
    --title-green: #44cc55;
    --title-coral: #ff6048;
    --art-warm: #e8664f;
    --art-soft: #e6e2dc;
  }
  html, body {
    margin: 0;
    padding: 0;
    width: 1200px;
    height: 1200px;
    overflow: hidden;
    background: var(--page-bg);
  }
  .book-cover {
    position: absolute;
    left: 280px;
    top: 88px;
    width: 640px;
    height: 1024px;
    background: var(--cover-bg);
  }
  .book-cover svg {
    display: block;
    width: 100%;
    height: 100%;
  }
  .kicker { font-family: "Outfit", sans-serif; font-weight: 400; fill: var(--ink-dark); }
  .lead { font-family: "Outfit", sans-serif; font-weight: 700; fill: var(--accent-blue); }
  .title-main { font-family: "Bebas Neue", sans-serif; }
  .title-second { font-family: "Bebas Neue", sans-serif; fill: var(--title-coral); }
  .subtitle { font-family: "Outfit", sans-serif; font-weight: 600; fill: var(--ink-text); letter-spacing: 0.5px; }
  .author { font-family: "Outfit", sans-serif; font-weight: 500; fill: var(--ink-text); letter-spacing: 1px; }
</style>
</head>
<body>
  <div class="book-cover">
    <svg viewBox="0 0 640 1024" xmlns="http://www.w3.org/2000/svg">
      <defs>
        <linearGradient id="title-gradient" gradientUnits="userSpaceOnUse" x1="0" y1="222" x2="0" y2="452">
          <stop offset="0" stop-color="var(--title-green)"/>
          <stop offset="0.15" stop-color="var(--title-green)"/>
          <stop offset="0.75" stop-color="var(--title-coral)"/>
          <stop offset="1" stop-color="var(--title-coral)"/>
        </linearGradient>
        <radialGradient id="art-gradient" cx="0.45" cy="0.5" r="0.6">
          <stop offset="0" stop-color="var(--art-warm)" stop-opacity="0.55"/>
          <stop offset="0.6" stop-color="var(--art-soft)" stop-opacity="0.7"/>
          <stop offset="1" stop-color="var(--cover-bg)" stop-opacity="0"/>
        </radialGradient>
      </defs>

      <text class="kicker" x="54" y="146" font-size="48">lessons</text>
      <text class="lead" x="54" y="204" font-size="58" textLength="266" lengthAdjust="spacingAndGlyphs">FROM THE</text>

      <text class="title-main" x="52" y="452" font-size="330" fill="url(#title-gradient)" textLength="540" lengthAdjust="spacingAndGlyphs">SILENT</text>
      <text class="title-second" x="54" y="588" font-size="175" textLength="528" lengthAdjust="spacingAndGlyphs">ORCHARD</text>

      <text class="subtitle" x="320" y="642" font-size="21" text-anchor="middle">MINDSET - INSIGHTS - SKILLS &amp; TOOLS</text>

      <rect class="cover-art" x="84" y="680" width="496" height="208" rx="40" fill="url(#art-gradient)" role="img" aria-label="Photo of a small turtle on toy wheels with a red rocket strapped to its back, leaving a trail of smoke"/>

      <text class="author" x="334" y="976" font-size="40" text-anchor="middle">MAARTEN DE KLERK</text>
    </svg>
  </div>
</body>
</html>
```